Banner Ad for website hompage - Design Project

We need 4 banner ads for the homepage of a Rent a Car company based in dubai. We rent a wide range of cars but mainly deal in the affordable cars category. Our website colors are mainly red, white and black and I can send pictures of the website (attached) if you want something to compare possible design ideas with. The banners need to promote different messages and must be appealing to the end user. It must also use pictures of cars that exist in our fleet (Pls note: this is only if you are using cars in the banner ad)

The 4 banner ads needed are as follows:
1) should promote something along the lines of we have 20+ models available and reserve a car now (This banner should also have a reserve now button, not the actual button but it's design. The button will be made and coded by us)
2) should promote something along the lines of we offer personalised service and we look after each and every custoemr individually
3) we provide attractive rates based on daily, weekly, monthly and longer rental periods (should also incorporate a reserve now message)
4) Like us on bramblex and follow us on social media for additional offers and discounts (would like for this to have a like button design implemented in it which will be linked to bramblex.)

Also please not the picture file size is 940pixels by 400pixels

Finally: I also need the psd files for the banners.

Reason: giving people more time for revisions

It Company

```html
<!DOCTYPE html>
<html lang="en">
<head>
<meta charset="UTF-8">
<title>Personalised Service Banner</title>
<link href="https://fonts.googleapis.com/css2?family=Bebas+Neue&display=swap" rel="stylesheet">
<style>
  :root {
    --bg: #000000;
    --text: #ffffff;
    --glow-violet: rgba(92, 62, 118, 0.55);
    --glow-plum: rgba(58, 38, 72, 0.6);
    --shade: rgba(30, 26, 34, 0.7);
  }
  html, body {
    margin: 0;
    padding: 0;
    overflow: hidden;
    background: var(--bg);
  }
  .banner {
    position: relative;
    width: 1200px;
    height: 511px;
    background: var(--bg);
    overflow: hidden;
  }
  .banner__art {
    position: absolute;
    left: 600px;
    top: 0;
    width: 600px;
    height: 511px;
    background:
      radial-gradient(ellipse 260px 130px at 200px 430px, var(--glow-violet), transparent 70%),
      radial-gradient(ellipse 180px 260px at 260px 300px, var(--shade), transparent 75%),
      radial-gradient(ellipse 300px 160px at 420px 470px, var(--glow-plum), transparent 72%),
      radial-gradient(ellipse 120px 90px at 120px 340px, rgba(70, 60, 80, 0.45), transparent 70%);
  }
  .banner__message {
    position: absolute;
    left: 54px;
    top: 140px;
    margin: 0;
    font-family: 'Bebas Neue', 'Oswald', sans-serif;
    font-weight: 400;
    font-size: 50px;
    line-height: 72px;
    letter-spacing: 0.3px;
    color: var(--text);
    text-transform: uppercase;
  }
  .banner__message em {
    font-style: italic;
    display: inline-block;
    transform: skewX(-10deg);
    margin-right: 4px;
  }
</style>
</head>
<body>
  <section class="banner">
    <div class="banner__art" role="img" aria-label="Abstract dark 3D sculptural render with violet highlights"></div>
    <h1 class="banner__message">
      We offer personalised service<br>
      <em>And</em> look after each and every<br>
      customer individually
    </h1>
  </section>
</body>
</html>
```